Sleep/Snoring Business - Requires Website - Australia

We are seeking a simple to maintain website for our sleep business. The health care business provides diagnostic and treatment solutions for snoring, sleep disorders and other respiratory problems.

Ideally, colours to match the company logo (attached).

The page must be built using WORDPRESS.

Ideally site will have a home page outlining the business, with 5 sub pages - being "Diagnosis" "Treatment Options", "Prodcuts", "About Us", "Contact Us"

The site home page should include a large picture on the home page.

The "Treatment Options" and "Diagnosis" pages must include:
Allow for a few pictures with assocaited text, plus space for some embeded youtube videos.

"Prodcuts" page should have the ability to show 3-4 products across the page with text below.. that can include external URL to products

The "About Us" page must include:
1. a Map (google map) to identify the various locations. There are 6 in total.
2. A Section to describe our doctors/staff - allow for a picture and some text

The "Contact Us" page must include:
email form
telephone details

The overall design should have a clean and medical/safe feeling

People who snore and those with sleeping and respiratory disorders

Health Care

• The page must be built using WORDPRESS.
• Ideally site will have a home page outlining the business, with 5 sub pages - being "Diagnosis" "Treatment Options", "Prodcuts", "About Us", "Contact Us"
• The site home page should include a large picture on the home page.
• The "Treatment Options" and "Diagnosis" pages must include:
• Allow for a few pictures with assocaited text, plus space for some embeded youtube videos.
• "Prodcuts" page should have the ability to show 3-4 products across the page with text below.. that can include external URL to products
• The "About Us" page must include:
• 1. a Map (google map) to identify the various locations. There are 6 in total.
• 2. A Section to describe our doctors/staff - allow for a picture and some text
• The "Contact Us" page must include:
• email form
• telephone details
• Pictures must be licenced or free to use
• Home page pictures showing people sleeping well, snoring or fresh air (landscape) type transition pictures (at least 3).
• Not to look cheap
• This is a high end healthcare business, so must look that way

```html
<!DOCTYPE html>
<html lang="en">
<head>
<meta charset="utf-8">
<title>Restwell Clinics — Home</title>
<link rel="stylesheet" href="https://fonts.googleapis.com/css2?family=Poppins:wght@500;600&family=Arimo:wght@400;700&display=swap">
<style>
  :root {
    --header-bg: #252a31;
    --badge-bg: #1d2126;
    --brand-blue: #1b5fa0;
    --nav-active: #2aa3d8;
    --nav-text: #ffffff;
    --footer-bg: #154a7c;
    --footer-text: #ffffff;
    --headline: #2b2b2b;
    --dot-active: #154a7c;
    --dot: #5c6168;
    --hero-top: #a3c5f0;
    --hero-bottom: #dfe6ee;
  }
  * { margin: 0; padding: 0; box-sizing: border-box; }
  html, body { width: 1200px; height: 827px; overflow: hidden; }
  body { position: relative; font-family: "Poppins", sans-serif; background: #fff; }

  .hero {
    position: absolute; left: 0; top: 82px; width: 1200px; height: 660px;
    background: linear-gradient(180deg, var(--hero-top) 0%, var(--hero-bottom) 100%);
  }
  .hero-headline {
    position: absolute; right: 164px; top: 243px; text-align: right;
    font-size: 28px; font-weight: 600; line-height: 41px; color: var(--headline);
    text-shadow: 0 0 10px rgba(255,255,255,.9), 0 0 4px rgba(255,255,255,.8);
  }
  .slider-dots { position: absolute; left: 970px; top: 416px; display: flex; gap: 7px; }
  .slider-dots span { width: 10px; height: 10px; border-radius: 50%; background: var(--dot); }
  .slider-dots span.is-active { background: var(--dot-active); }

  .site-header { position: absolute; left: 0; top: 0; width: 1200px; height: 82px; background: var(--header-bg); }
  .main-nav a {
    position: absolute; top: 28px; font-size: 13px; font-weight: 600; letter-spacing: -0.1px;
    color: var(--nav-text); text-decoration: none; white-space: nowrap;
  }
  .main-nav a.is-current { color: var(--nav-active); }
  .nav-sep { position: absolute; top: 26px; width: 1px; height: 22px; background: #6a7078; }

  .brand-badge {
    position: absolute; left: 475px; top: -72px; width: 225px; height: 225px;
    border-radius: 50%; background: var(--badge-bg);
    display: flex; align-items: flex-end; justify-content: center; padding-bottom: 64px;
  }
  .brand-name { font-size: 30px; font-weight: 600; color: var(--brand-blue); white-space: nowrap; }

  .site-footer { position: absolute; left: 0; top: 742px; width: 1200px; height: 85px; background: var(--footer-bg); color: var(--footer-text); font-family: "Arimo", sans-serif; }
  .contact-line { position: absolute; left: 161px; top: 20px; display: flex; align-items: center; font-size: 12.5px; }
  .contact-item { display: flex; align-items: center; gap: 6px; }
  .contact-sep { width: 1px; height: 20px; background: rgba(255,255,255,.55); margin: 0 12px; }
  .copyright { position: absolute; left: 163px; top: 54px; font-size: 11px; }
  .follow-title { position: absolute; left: 913px; top: 17px; font-size: 15px; font-weight: 700; }
  .social-list { position: absolute; left: 912px; top: 42px; display: flex; gap: 7px; }
  .social-list a {
    width: 26px; height: 26px; border: 1.5px solid #fff; border-radius: 50%;
    display: flex; align-items: center; justify-content: center;
    color: #fff; text-decoration: none; font-size: 9px; font-weight: 700;
  }
</style>
</head>
<body>
  <section class="hero" role="img" aria-label="Photo of a woman in a white shirt with arms outstretched, breathing fresh air outdoors">
    <h1 class="hero-headline">We are seeking a simple to<br>maintain website for our<br>sleep business</h1>
    <div class="slider-dots"><span class="is-active"></span><span></span><span></span><span></span></div>
  </section>

  <header class="site-header">
    <nav class="main-nav">
      <a href="#" class="is-current" style="left:159px">Home</a>
      <i class="nav-sep" style="left:215px"></i>
      <a href="#" style="left:234px">Diagnosis</a>
      <i class="nav-sep" style="left:314px"></i>
      <a href="#" style="left:331px">Treatment Options</a>
      <a href="#" style="left:736px">Prodcuts</a>
      <i class="nav-sep" style="left:820px"></i>
      <a href="#" style="left:850px">About Us</a>
      <i class="nav-sep" style="left:938px"></i>
      <a href="#" style="left:967px">Contact Us</a>
    </nav>
    <div class="brand-badge"><span class="brand-name">Restwell</span></div>
  </header>

  <footer class="site-footer">
    <div class="contact-line">
      <span class="contact-item">
        <svg width="9" height="12" viewBox="0 0 9 12"><path d="M4.5 0A4.5 4.5 0 0 0 0 4.5C0 8 4.5 12 4.5 12S9 8 9 4.5A4.5 4.5 0 0 0 4.5 0Zm0 6.3a1.8 1.8 0 1 1 0-3.6 1.8 1.8 0 0 1 0 3.6Z" fill="#fff"/></svg>
        Lorem ipsum dolor sit amet, consectetuer - 012345
      </span>
      <i class="contact-sep"></i>
      <span class="contact-item">
        <svg width="11" height="11" viewBox="0 0 24 24"><path d="M6.6 10.8a15 15 0 0 0 6.6 6.6l2.2-2.2c.3-.3.7-.4 1-.2 1.1.4 2.3.6 3.6.6.6 0 1 .4 1 1V20c0 .6-.4 1-1 1A17 17 0 0 1 3 4c0-.6.4-1 1-1h3.5c.6 0 1 .4 1 1 0 1.3.2 2.5.6 3.6.1.3 0 .7-.2 1l-2.3 2.2Z" fill="#fff"/></svg>
        013-246-5780
      </span>
      <i class="contact-sep"></i>
      <span class="contact-item">
        <svg width="12" height="9" viewBox="0 0 12 9"><rect width="12" height="9" rx="1" fill="#fff"/><path d="M.5 .8 6 5l5.5-4.2" stroke="#154a7c" stroke-width="1.2" fill="none"/></svg>
        info@restwellclinics.com
      </span>
    </div>
    <p class="copyright">Copyright© 2017 Restwell Clinics. All right reserved.</p>
    <p class="follow-title">Follow us:</p>
    <nav class="social-list" aria-label="Social links">
      <a href="#" title="Nookly">Nk</a>
      <a href="#" title="Chirpa">Ch</a>
      <a href="#" title="Plazo">Pz</a>
      <a href="#" title="Vocara">Vo</a>
    </nav>
  </footer>
</body>
</html>
```